Web Design Project for a beach town business owner who supports new families with their babies.

I'm looking for a basic website with the following pages: home, about, services, FAQs, blog, and contact page. I have images and content ready to go.

Target Market(s)

Men and women between the ages of 22 and 42, growing families

Industry/Entity Type

Postpartum Doula

Coding

Number of Pages Required

5+ page

Font styles to use
Serif
Other font styles liked:
• My logo font is "Nexa Bold" - so coordinating fonts with that are ideal

Colors
00AB8E
00BBA5
67D7C9
C6EFE9
E9F9F6
EE7325
F08F49
F5BC92
FAE3D3
FDF4ED

Requirements
Must have
• Warm and professional vibe, multicultural images, aligned with my branding colors and font ("Nexa Bold"; COLORS: light blue hex: #2FCEC2 R: 47 G: 206 B: 194 dark blue hex: #007C7C R: 0 G: 124 B: 124 orange hex: #F77B4E R: 247 G: 123 B: 78), good SEO
Should not have
• Ultra feminine images, baby bottles, cutesy images.

```html
<!DOCTYPE html>
<html lang="en">
<head>
<meta charset="utf-8">
<title>Tidewell Families Postpartum Care</title>
<link href="https://fonts.googleapis.com/css2?family=Montserrat:wght@600;700;800&family=Open+Sans:wght@400;600;700&display=swap" rel="stylesheet">
<style>
:root{
  --teal-dark:#007C7C;
  --teal:#00AB8E;
  --teal-mid:#00BBA5;
  --teal-light:#67D7C9;
  --teal-pale:#C6EFE9;
  --teal-mist:#E9F9F6;
  --orange:#EE7325;
  --orange-soft:#F08F49;
  --ink:#2b2b2b;
  --grey:#6d6d6d;
  --footer:#262626;
  --white:#ffffff;
}
*{box-sizing:border-box;margin:0;padding:0}
html,body{width:1200px;height:3544px;overflow:hidden;background:var(--white)}
body{position:relative;font-family:"Open Sans",Arial,sans-serif;color:var(--ink)}
.heading{font-family:"Montserrat",Arial,sans-serif;font-weight:800;letter-spacing:2px}
.btn{display:inline-block;background:var(--orange);color:var(--white);font-family:"Montserrat",Arial,sans-serif;font-weight:700;font-size:15px;letter-spacing:1px;border-radius:30px;padding:20px 40px;text-decoration:none;box-shadow:0 6px 14px rgba(0,0,0,.18)}

/* header */
.site-header{position:absolute;top:0;left:0;width:1200px;height:110px;z-index:5}
.brand-badge{position:absolute;left:112px;top:-6px;width:140px;height:140px;border-radius:50%;background:var(--white);border:5px solid var(--teal);display:flex;align-items:center;justify-content:center;text-align:center;font-family:"Montserrat",Arial,sans-serif;font-weight:700;font-size:17px;line-height:1.2;color:var(--teal-dark);padding:18px}
.main-nav{position:absolute;right:76px;top:0;display:flex;align-items:center;height:100px}
.main-nav a{font-family:"Montserrat",Arial,sans-serif;font-weight:700;font-size:15px;color:var(--white);text-decoration:none;padding:0 16px;height:100px;display:flex;align-items:center}
.main-nav a.active{background:var(--teal)}
.search-dot{width:34px;height:34px;border-radius:50%;background:var(--orange);margin-left:14px;display:flex;align-items:center;justify-content:center}

/* hero */
.hero{position:absolute;top:0;left:0;width:1200px;height:800px}
.hero-photo{position:absolute;inset:0;background:radial-gradient(circle at 78% 32%,#c98a6a 0,#8a5f48 12%,transparent 30%),linear-gradient(120deg,#2f4a2d 0%,#4e6b3a 40%,#3f5f38 70%,#223a26 100%)}
.hero-shade{position:absolute;inset:0;background:linear-gradient(90deg,rgba(0,0,0,.35),rgba(0,0,0,.05))}
.hero-copy{position:absolute;left:145px;top:330px;color:var(--white)}
.hero-title{font-size:76px;line-height:1;margin-bottom:52px}
.hero-sub{font-family:"Montserrat",Arial,sans-serif;font-weight:700;font-size:21px;line-height:1.5;width:520px;margin-bottom:58px}
.hero-dots{position:absolute;right:46px;top:396px;display:flex;flex-direction:column;gap:14px}
.hero-dots span{width:8px;height:8px;border-radius:50%;background:rgba(255,255,255,.6)}
.hero-dots span:first-child{background:var(--white)}
.hero-wave{position:absolute;left:0;top:640px}

/* about */
.about{position:absolute;top:790px;left:0;width:1200px;height:540px}
.about-photo{position:absolute;left:176px;top:30px;width:344px;height:344px;border-radius:50%;border:10px solid var(--teal);background:radial-gradient(circle at 45% 40%,#d6a486 0,#b97f62 22%,#6c4a3c 45%,#e7e0d8 70%)}
.about-copy{position:absolute;left:598px;top:110px;width:530px}
.about-title{font-size:44px;color:var(--ink);margin-bottom:20px}
.about-text{font-size:13.5px;line-height:1.62;color:var(--grey)}
.about .btn{margin:32px 0 0 4px;padding:16px 32px;font-size:14px}

/* services */
.services{position:absolute;top:1300px;left:0;width:1200px;height:860px}
.services-bg{position:absolute;top:120px;left:0;width:1200px;height:600px;background:linear-gradient(135deg,#0c8a78,#00AB8E 45%,#0a9c84)}
.services-title{position:absolute;top:240px;width:100%;text-align:center;color:var(--white);font-size:48px}
.service-list{position:absolute;top:400px;left:140px;width:920px;display:flex;justify-content:space-between}
.service{width:170px;text-align:center;color:var(--white);font-family:"Montserrat",Arial,sans-serif;font-weight:700;font-size:14px;line-height:1.3}
.service-icon{width:150px;height:150px;border-radius:50%;border:4px solid var(--white);margin:0 auto 18px;display:flex;align-items:center;justify-content:center}
.slider-arrow{position:absolute;top:460px;width:20px;height:36px}

/* faq */
.faq{position:absolute;top:2150px;left:0;width:1200px;height:1060px}
.faq-bg{position:absolute;top:60px;left:0;width:1200px;height:1000px;background:linear-gradient(180deg,#f3f6f4,#e8ece8 40%,#eef2ef);opacity:.9}
.faq-title{position:absolute;top:88px;width:100%;text-align:center;font-size:48px;color:var(--ink)}
.faq-list{position:absolute;top:192px;left:300px;width:660px;list-style:none}
.faq-item{background:var(--white);border-radius:4px;margin-bottom:14px;box-shadow:0 2px 6px rgba(0,0,0,.12)}
.faq-q{display:flex;justify-content:space-between;align-items:center;padding:14px 16px;font-size:14px;font-weight:600;color:var(--ink)}
.faq-toggle{width:24px;height:24px;border-radius:50%;background:var(--orange);color:var(--white);font-weight:700;display:flex;align-items:center;justify-content:center;font-size:16px;line-height:1}
.faq-a{padding:6px 16px 22px;font-size:12.5px;line-height:1.6;color:var(--grey);border-top:1px solid #eee}

/* footer */
.site-footer{position:absolute;top:3180px;left:0;width:1200px;height:364px}
.footer-band{position:absolute;top:0;left:0}
.footer-badge{position:absolute;left:120px;top:78px;width:180px;height:180px;border-radius:50%;background:var(--white);border:6px solid var(--teal);display:flex;align-items:center;justify-content:center;text-align:center;font-family:"Montserrat",Arial,sans-serif;font-weight:700;font-size:21px;line-height:1.2;color:var(--teal-dark);padding:22px}
.footer-nav{position:absolute;right:140px;top:156px;display:flex;gap:30px}
.footer-nav a{color:var(--white);text-decoration:none;font-family:"Montserrat",Arial,sans-serif;font-weight:700;font-size:17px}
.footer-social{position:absolute;left:418px;top:252px;display:flex;gap:14px}
.footer-social span{width:34px;height:34px;border-radius:50%;border:2px solid var(--white)}
.footer-legal{position:absolute;left:418px;top:320px;font-size:11px;color:#bdbdbd}
</style>
</head>
<body>

<header class="site-header">
  <div class="brand-badge">Tidewell Families</div>
  <nav class="main-nav">
    <a class="active" href="#">HOME</a>
    <a href="#">ABOUT</a>
    <a href="#">SERVICES</a>
    <a href="#">FAQS</a>
    <a href="#">BLOG</a>
    <a href="#">CONTACT</a>
    <span class="search-dot"><svg width="16" height="16" viewBox="0 0 16 16"><circle cx="6.5" cy="6.5" r="4.5" fill="none" stroke="#fff" stroke-width="2"/><line x1="10" y1="10" x2="14" y2="14" stroke="#fff" stroke-width="2"/></svg></span>
  </nav>
</header>

<section class="hero">
  <div class="hero-photo" role="img" aria-label="Photo of a smiling postpartum care expert outdoors among green trees"></div>
  <div class="hero-shade"></div>
  <div class="hero-copy">
    <h1 class="heading hero-title">TIDEWELL<br>FAMILIES</h1>
    <p class="hero-sub">Congratulations on your birth and welcome to Tidewell Families Postpartum Care!</p>
    <a class="btn" href="#">GET STARTED</a>
  </div>
  <div class="hero-dots"><span></span><span></span><span></span></div>
  <svg class="hero-wave" width="1200" height="160" viewBox="0 0 1200 160">
    <path d="M0 90 C260 170 520 150 760 110 C960 76 1100 40 1200 20 L1200 160 L0 160Z" fill="#00AB8E"/>
    <path d="M0 112 C260 186 520 166 760 128 C960 96 1100 64 1200 44 L1200 160 L0 160Z" fill="#fff"/>
  </svg>
</section>

<section class="about">
  <div class="about-photo" role="img" aria-label="Portrait of the care expert holding a newborn baby"></div>
  <div class="about-copy">
    <h2 class="heading about-title">ABOUT</h2>
    <p class="about-text">Hi, I'm Dana Reyes, a certified postpartum care expert and educator serving families of all varieties in the greater bay area and beyond. My passion as a professional is showing new parents just like you that whether you just had your first child or your fifth, you can not only survive your postpartum period but thrive in the early weeks. I offer calm, practical and tailored support for your unique needs, right in your own home. That's where I come in.<br>Did you know that, on average, new parents won't see their midwife or obstetrician until six weeks after giving birth to their babies? Working with a postpartum care expert helps bridge that gap so you can rest, recover and bond with confidence.</p>
    <a class="btn" href="#">READ MORE</a>
  </div>
</section>

<section class="services">
  <svg style="position:absolute;top:0;left:0" width="1200" height="860" viewBox="0 0 1200 860">
    <path d="M0 60 C300 10 560 40 800 20 C980 6 1100 0 1200 10 L1200 200 L0 200Z" fill="#00AB8E"/>
    <path d="M0 700 L1200 700 L1200 740 C1000 840 760 800 560 780 C340 758 160 800 0 820Z" fill="#00AB8E"/>
  </svg>
  <div class="services-bg" role="img" aria-label="Faded photo of the care expert with a family, tinted teal"></div>
  <h2 class="heading services-title">OUR SERVICES</h2>
  <svg class="slider-arrow" style="left:60px" viewBox="0 0 20 36"><polyline points="18,2 2,18 18,34" fill="none" stroke="#C6EFE9" stroke-width="3"/></svg>
  <svg class="slider-arrow" style="right:60px" viewBox="0 0 20 36"><polyline points="2,2 18,18 2,34" fill="none" stroke="#C6EFE9" stroke-width="3"/></svg>
  <div class="service-list">
    <div class="service"><div class="service-icon"><svg width="70" height="70" viewBox="0 0 70 70" fill="none" stroke="#fff" stroke-width="3"><rect x="14" y="24" width="42" height="36" rx="4"/><line x1="14" y1="34" x2="56" y2="34"/><rect x="24" y="12" width="22" height="12" rx="2"/></svg></div>WASH AND FOLD<br>LAUNDRY</div>
    <div class="service"><div class="service-icon"><svg width="70" height="70" viewBox="0 0 70 70" fill="none" stroke="#fff" stroke-width="3"><line x1="40" y1="8" x2="30" y2="40"/><path d="M18 40 L42 40 L48 62 L12 62Z"/></svg></div>TIDY UP COMMON<br>LIVING SPACE</div>
    <div class="service"><div class="service-icon"><svg width="70" height="70" viewBox="0 0 70 70" fill="none" stroke="#fff" stroke-width="3"><rect x="14" y="10" width="42" height="52" rx="3"/><line x1="14" y1="22" x2="56" y2="22"/><rect x="22" y="30" width="26" height="24"/></svg></div>LOAD/UNLOAD<br>DISHWASHER</div>
    <div class="service"><div class="service-icon"><svg width="70" height="70" viewBox="0 0 70 70" fill="none" stroke="#fff" stroke-width="3"><line x1="14" y1="18" x2="56" y2="18"/><rect x="28" y="10" width="14" height="8"/><path d="M18 18 L22 62 L48 62 L52 18"/><line x1="30" y1="28" x2="30" y2="54"/><line x1="40" y1="28" x2="40" y2="54"/></svg></div>TAKE TRASH<br>OUT</div>
  </div>
</section>

<section class="faq">
  <div class="faq-bg" role="img" aria-label="Soft, faded photo of the care expert with a smiling client"></div>
  <h2 class="heading faq-title">FAQS</h2>
  <ul class="faq-list">
    <li class="faq-item"><div class="faq-q">What is a postpartum care expert (doula)? <span class="faq-toggle">&minus;</span></div>
      <p class="faq-a">A postpartum care expert is a professional who provides non-medical support to families in the weeks after birth. Typical services include easing the new-parent transition, light household tasks, feeding guidance, newborn care tips and helping you rest and recover at home.</p></li>
    <li class="faq-item"><div class="faq-q">Do you provide nanny services? <span class="faq-toggle">+</span></div></li>
    <li class="faq-item"><div class="faq-q">What kinds of medical support can you offer? <span class="faq-toggle">+</span></div></li>
    <li class="faq-item"><div class="faq-q">Are you available for overnight shifts? <span class="faq-toggle">+</span></div></li>
    <li class="faq-item"><div class="faq-q">What if I have my baby prematurely and they are admitted to the NICU? <span class="faq-toggle">+</span></div></li>
    <li class="faq-item"><div class="faq-q">I had a surgical birth. How can you support me? <span class="faq-toggle">+</span></div></li>
    <li class="faq-item"><div class="faq-q">Are there any services you don't provide? <span class="faq-toggle">+</span></div></li>
    <li class="faq-item"><div class="faq-q">How long can I expect to work with a postpartum care expert? <span class="faq-toggle">+</span></div></li>
    <li class="faq-item"><div class="faq-q">What precautions do you take to reduce the likelihood of spreading germs to my family? <span class="faq-toggle">+</span></div></li>
    <li class="faq-item"><div class="faq-q">This sounds great! How do I book your services? <span class="faq-toggle">+</span></div></li>
  </ul>
</section>

<footer class="site-footer">
  <svg class="footer-band" width="1200" height="364" viewBox="0 0 1200 364">
    <path d="M0 70 C300 110 620 40 900 60 C1040 70 1130 90 1200 80 L1200 364 L0 364Z" fill="#262626"/>
  </svg>
  <div class="footer-badge">Tidewell Families</div>
  <nav class="footer-nav">
    <a href="#">HOME</a><a href="#">ABOUT</a><a href="#">SERVICES</a><a href="#">FAQS</a><a href="#">BLOG</a><a href="#">CONTACT</a>
  </nav>
  <div class="footer-social"><span></span><span></span><span></span><span></span><span></span></div>
  <p class="footer-legal">&copy; 2023 Tidewell Families. All rights reserved. &nbsp;|&nbsp; Privacy &nbsp;|&nbsp; Terms of Use</p>
</footer>

</body>
</html>
```